An international wholesale business needs letterhead design

Logo file is attached. Please design a letterhead with the following details:

- Company Name and Logo
- Address
- VAT Registration number
- Phone No
- Website address

```html
<!DOCTYPE html>
<html lang="en">
<head>
<meta charset="utf-8">
<title>Velora Trading – Stationery</title>
<link rel="stylesheet" href="https://fonts.googleapis.com/css2?family=Poppins:wght@400;500;600&family=Open+Sans:wght@400&display=swap">
<style>
  :root {
    --red: #c32530;
    --red-soft: #c8423c;
    --ink: #1d1d1f;
    --grey: #8c8f94;
    --rule: #9a9a9a;
    --paper: #ffffff;
    --bg-top: #fafafa;
    --bg-bottom: #e8e8ea;
  }
  * { margin: 0; padding: 0; box-sizing: border-box; }
  html, body { width: 1200px; height: 1000px; overflow: hidden; }
  body {
    position: relative;
    background: linear-gradient(180deg, var(--bg-top), var(--bg-bottom));
    font-family: "Poppins", sans-serif;
    color: var(--ink);
  }
  .showcase-title {
    position: absolute; top: 247px; left: 0; width: 100%;
    text-align: center; font-family: "Open Sans", sans-serif;
    font-size: 20px; color: #ffffff; letter-spacing: 0.3px;
  }
  .sheet { position: absolute; background: var(--paper); overflow: hidden; }

  /* brand name */
  .brand {
    position: absolute; display: flex; align-items: center; gap: 4px;
    font-family: "Poppins", sans-serif; font-weight: 600; font-size: 9px;
    color: var(--red); letter-spacing: 0.4px; text-transform: uppercase; white-space: nowrap;
  }
  .brand-dot {
    width: 14px; height: 14px; border-radius: 50%;
    border: 1.6px solid var(--red);
  }
  .brand--white { color: #fff; }

  /* contact block */
  .contact {
    position: absolute; font-size: 4.8px; line-height: 5.4px; color: var(--ink);
  }
  .contact .row { display: flex; align-items: center; gap: 4px; margin-top: 2.3px; }
  .contact svg { width: 4px; height: 4px; fill: var(--red); }

  /* envelope front */
  .envelope-front { left: 100px; top: 329px; width: 342px; height: 149px; }
  .envelope-front .brand { left: 27px; top: 18px; }
  .envelope-front .contact { left: 248px; top: 18px; }
  .envelope-front .band-rule { position: absolute; left: 0; right: 0; top: 124px; height: 1px; background: var(--red); }
  .envelope-front .band {
    position: absolute; left: 0; right: 0; top: 126px; bottom: 0; background: var(--red);
    display: flex; align-items: center; justify-content: center; gap: 22px;
    color: #fff; font-size: 6.2px;
  }
  .band .item { display: flex; align-items: center; gap: 7px; }
  .band svg { width: 5px; height: 5px; fill: #fff; }

  /* envelope back */
  .envelope-back { left: 100px; top: 518px; width: 342px; height: 148px; }
  .envelope-back .flap {
    position: absolute; left: 0; right: 0; top: 0; height: 32px; background: var(--red);
    border-radius: 0 0 32px 32px; display: flex; align-items: center; justify-content: center;
  }
  .envelope-back .flap .brand { position: static; font-size: 8.5px; }
  .envelope-back .brand--corner { right: 28px; top: 117px; font-size: 8.5px; }

  /* letter */
  .letter { left: 473px; top: 329px; width: 298px; height: 421px; }
  .letter > .brand, .cover > .brand { left: 33px; top: 24px; }
  .letter > .contact, .cover > .contact { left: 211px; top: 23px; }
  .letter .divider { position: absolute; left: 23px; right: 23px; top: 69px; height: 0.6px; background: var(--rule); }
  .letter .text { position: absolute; left: 23px; right: 23px; font-size: 5px; line-height: 7.4px; }
  .letter .recipient { top: 83px; }
  .letter .recipient .addr { padding-left: 9.5px; }
  .letter .date { top: 83px; text-align: right; }
  .letter b { font-weight: 600; }
  .letter .subject { top: 138px; }
  .letter .subject-line { top: 167px; font-size: 4.2px; }
  .letter .greeting { top: 184px; }
  .letter .body { top: 203px; line-height: 9.5px; text-align: justify; }
  .letter .body p + p { margin-top: 9.5px; }
  .letter .closing { top: 322px; }
  .letter .sender { top: 352px; }
  .letter .brand--footer { right: 23px; top: 378px; font-size: 8.5px; }
  .letter .foot-rule { position: absolute; left: 0; right: 0; top: 398px; height: 1px; background: var(--red); }
  .letter .foot-band { position: absolute; left: 0; right: 0; top: 403px; bottom: 0; background: var(--red); }

  /* report cover */
  .cover { left: 802px; top: 329px; width: 298px; height: 421px; }
  .cover .rule { position: absolute; left: 0; right: 0; top: 136px; height: 1px; background: var(--red); }
  .cover .panel {
    position: absolute; left: 0; right: 0; top: 140px; bottom: 0; background: var(--red-soft);
    display: flex; flex-direction: column; align-items: center; justify-content: center;
    color: #fff; font-family: "Open Sans", sans-serif; text-align: center;
    padding-bottom: 18px;
  }
  .cover .doc-title { font-size: 23px; line-height: 23px; }
  .cover .doc-desc { font-size: 11px; margin-top: 3px; }
</style>
</head>
<body>
  <h1 class="showcase-title" style="font-weight:400">Letterhead Design</h1>

  <svg width="0" height="0" style="position:absolute">
    <defs>
      <symbol id="icon-globe" viewBox="0 0 10 10"><circle cx="5" cy="5" r="4.5"/><path d="M0.5 5h9M5 0.5v9" stroke="#fff" stroke-width="0.8"/></symbol>
      <symbol id="icon-phone" viewBox="0 0 10 10"><path d="M2 0.8l2 2-1 1.3c.6 1.3 1.6 2.3 2.9 2.9l1.3-1 2 2-1.2 1.4C4.6 9.2.8 5.4 0.6 2z"/></symbol>
      <symbol id="icon-home" viewBox="0 0 10 10"><path d="M5 0.8L0.5 5H2v4.2h2.3V6.5h1.4v2.7H8V5h1.5z"/></symbol>
    </defs>
  </svg>

  <!-- Envelope front -->
  <section class="sheet envelope-front">
    <div class="brand"><span class="brand-dot"></span>Velora Trading</div>
    <div class="contact">
      <div>P.O. Box 1234<br>Address, City 56789<br>VAT Reg. GB 123 4567 89</div>
      <div class="row"><svg><use href="#icon-globe"/></svg>www.website.com</div>
      <div class="row"><svg><use href="#icon-phone"/></svg>(01)234-5678</div>
    </div>
    <div class="band-rule"></div>
    <div class="band">
      <span class="item"><svg><use href="#icon-home"/></svg>P.O. Box 1234 Address, City 56789</span>
      <span class="item"><svg><use href="#icon-phone"/></svg>(01)234-5678</span>
      <span class="item"><svg><use href="#icon-globe"/></svg>www.website.com</span>
    </div>
  </section>

  <!-- Envelope back -->
  <section class="sheet envelope-back">
    <div class="flap"><div class="brand brand--white">Velora Trading</div></div>
    <div class="brand brand--corner">Velora Trading</div>
  </section>

  <!-- Letter -->
  <section class="sheet letter">
    <div class="brand"><span class="brand-dot"></span>Velora Trading</div>
    <div class="contact">
      <div>P.O. Box 1234<br>Address, City 56789<br>VAT Reg. GB 123 4567 89</div>
      <div class="row"><svg><use href="#icon-globe"/></svg>www.website.com</div>
      <div class="row"><svg><use href="#icon-phone"/></svg>(01)234-5678</div>
    </div>
    <div class="divider"></div>

    <div class="text recipient"><b>To : Ms. Partner</b><div class="addr">2200 E. Lake Road<br>67890 Sample City</div></div>
    <div class="text date"><b>Date :</b> January 04, 2021</div>

    <div class="text subject">Sample Document Subject<br>Department Sample</div>
    <div class="text subject-line">Here is the subject of the letter</div>
    <div class="text greeting">Dear Ms. Partner,</div>

    <div class="text body">
      <p>This is dummy text. It is only used to illustrate the gray value of the type. But is that really the case? Isn't it the same if I write "this is dummy text" or "Guaredisch nedunfeg"? Feguned – not at all.</p>
      <p>Dummy text provides important information, like the legibility of the body text, the impression it makes on the reader, the harmony between the individual figures, how narrow or wide they appear. Dummy text should contain as many different letters as possible and should be written in the original language. It doesn't have to make sense, it just needs to be readable. Texts in foreign languages, like "Lorem ipsum", don't actually serve this purpose, as they provide a false impression of what the body text actually looks like. This is dummy text. It is only used to illustrate the gray value of the type. But is that really the case? Isn't it the same if I write "this is dummy text" or "Guaredisch nedunfeg"? Feguned – not at all.</p>
    </div>

    <div class="text closing">Yours sincerely,<br>SAMPLE AG</div>
    <div class="text sender">NORDEN CARE GROUP</div>

    <div class="brand brand--footer">Velora Trading</div>
    <div class="foot-rule"></div>
    <div class="foot-band"></div>
  </section>

  <!-- Report cover -->
  <section class="sheet cover">
    <div class="brand"><span class="brand-dot"></span>Velora Trading</div>
    <div class="contact">
      <div>P.O. Box 1234<br>Address, City 56789<br>VAT Reg. GB 123 4567 89</div>
      <div class="row"><svg><use href="#icon-globe"/></svg>www.website.com</div>
      <div class="row"><svg><use href="#icon-phone"/></svg>(01)234-5678</div>
    </div>
    <div class="rule"></div>
    <div class="panel">
      <div class="doc-title">YOUR DOCUMENT<br>TITLE HERE</div>
      <div class="doc-desc">Description here</div>
    </div>
  </section>
</body>
</html>
```